Album Artwork for am orchestral Cuban Jazz somg

The artwork needs to be very classy and elegant and simple. The music is cuban jazz/orchestral chill music and I need something to convey that vibe
(https://www.vidplexa.example/watch?v=QrT4kL8wZ2n) this is very similar to the music I'm making and I would like it to have vintage vibe. Name of the track is (Adrift), artist are (Karim Sabet And Tarek Nouri)
Target Market(s)
People who listens to indie and jazz
Industry/Entity Type
Music
Font styles to use
Decorative
Script
Colors
Designer to choose only greyscale colors for use in the design.
Requirements
Must have
- vintage look, illustration and the font/name of the track/artist's name are the hero
Nice to have
- Hand written fonts which are rich and classy, latin dark vibes to it, minimalist, and I wanna feel its a cover for a 50s album
Should not have
- Computer fonts, any icons which has nothing to do with what I mentioned above, modern elements

```html
<!DOCTYPE html>
<html lang="en">
<head>
<meta charset="utf-8">
<title>Adrift — Karim Sabet &amp; Tarek Nouri</title>
<link href="https://fonts.googleapis.com/css2?family=Kaushan+Script&family=Bebas+Neue&display=swap" rel="stylesheet">
<style>
  :root {
    --stage: #5c5c5c;
    --stage-dark: #3f3f3f;
    --cover: #161616;
    --cover-edge: #101010;
    --ink: #ededed;
    --ink-soft: #d6d6d6;
    --frame: #cfcfcf;
    --blot: #2e2e2e;
  }
  html, body {
    margin: 0;
    padding: 0;
    width: 1200px;
    height: 589px;
    overflow: hidden;
  }
  body {
    background: radial-gradient(ellipse at 50% 40%, var(--stage) 0%, var(--stage-dark) 100%);
    display: flex;
    align-items: center;
    justify-content: center;
  }
  .album-cover {
    position: relative;
    width: 530px;
    height: 530px;
    background: radial-gradient(ellipse at 50% 35%, #1e1e1e 0%, var(--cover) 60%, var(--cover-edge) 100%);
    box-shadow: 0 6px 18px rgba(0,0,0,0.35);
    overflow: hidden;
  }
  .cover-frame {
    position: absolute;
    inset: 20px;
    border: 1px solid var(--frame);
    opacity: 0.85;
  }
  .ink-blot {
    position: absolute;
    left: 116px;
    top: 60px;
    width: 272px;
    height: 226px;
    border-radius: 46% 54% 40% 60% / 50% 42% 58% 50%;
    background: radial-gradient(ellipse at 50% 45%, var(--blot) 0%, rgba(46,46,46,0.6) 55%, rgba(46,46,46,0) 100%);
  }
  .track-title {
    position: absolute;
    left: 0;
    right: 0;
    top: 58px;
    margin: 0;
    text-align: center;
    font-family: 'Kaushan Script', cursive;
    font-weight: 400;
    font-size: 118px;
    line-height: 1;
    color: var(--ink);
    letter-spacing: -2px;
  }
  .suspension-line {
    position: absolute;
    left: 275px;
    top: 178px;
    width: 1px;
    height: 168px;
    background: var(--ink-soft);
  }
  .falling-figure {
    position: absolute;
    left: 262px;
    top: 344px;
    width: 28px;
    height: 34px;
    border-radius: 40%;
    background: linear-gradient(160deg, #e6e6e6, #bdbdbd);
  }
  .artists {
    position: absolute;
    left: 0;
    right: 0;
    top: 404px;
    margin: 0;
    text-align: center;
    font-family: 'Bebas Neue', sans-serif;
    font-size: 40px;
    line-height: 44px;
    letter-spacing: 0.2em;
    color: var(--ink);
  }
  .artists span { display: block; }
</style>
</head>
<body>
  <main class="album-cover">
    <div class="cover-frame"></div>
    <div class="ink-blot" role="img" aria-label="Faint grey watercolour stain behind the title"></div>
    <h1 class="track-title">adrift</h1>
    <div class="suspension-line"></div>
    <div class="falling-figure" role="img" aria-label="Small white illustration of a figure hanging upside down from the line"></div>
    <p class="artists">
      <span>Karim Sabet</span>
      <span>Tarek Nouri</span>
    </p>
  </main>
</body>
</html>
```